A5 5mm Grid and Dot Grid Page Layout

I need 2 designs:
1] A5 (5.75" x 8" inches final trimmed page size ) 128 journal pages with a 5mm x 5mm grid layout
2} A5 (5.75" x 8" inches final trimmed page size) 128 journal pages with 5mm x 5mm dot grid layout
First and last page should be blank
grid and dot grid should be a light gray color
Final design should you in PDF format

Target Market(s)

Fountain Pen Notebooks

Industry/Entity Type

Notebooks and Journals

Colors

Designer to choose only greyscale colors for use in the design.

Requirements
Must have
• Light gray 5mm x 5mm grid and dot grid page layout. Very thin lines
Should not have
• Thick black grid or dots

```html
<!DOCTYPE html>
<html lang="en">
<head>
<meta charset="UTF-8">
<title>A5 Grid and Dot Grid Page Layout</title>
<link href="https://fonts.googleapis.com/css2?family=Barlow+Semi+Condensed:wght@500&display=swap" rel="stylesheet">
<style>
  :root {
    --backdrop: #c6c5c6;
    --paper: #ffffff;
    --grid-line: #d2d2d2;
    --dot: #a9a9a9;
    --dimension: #707070;
    --label: #5e5e5e;
  }
  html, body {
    margin: 0;
    padding: 0;
    width: 1200px;
    height: 802px;
    overflow: hidden;
    background: var(--backdrop);
  }
  .spec-sheet {
    display: block;
    width: 1200px;
    height: 802px;
  }
  .page { fill: var(--paper); }
  .grid-frame { fill: none; stroke: var(--grid-line); stroke-width: 1.2; }
  .dim-line { stroke: var(--dimension); stroke-width: 2; fill: none; }
  .ext-line { stroke: var(--dimension); stroke-width: 1.6; }
  .dim-label {
    font-family: "Barlow Semi Condensed", "Roboto Condensed", sans-serif;
    font-weight: 500;
    font-size: 25px;
    fill: var(--label);
    text-anchor: middle;
    dominant-baseline: central;
  }
  .dim-gap { fill: var(--backdrop); }
</style>
</head>
<body>
<svg class="spec-sheet" viewBox="0 0 2100 1403" xmlns="http://www.w3.org/2000/svg">
  <defs>
    <marker id="arrow-end" viewBox="0 0 10 10" refX="9" refY="5" markerWidth="5" markerHeight="5" orient="auto-start-reverse">
      <path d="M0,1 L9,5 L0,9" fill="none" stroke="#707070" stroke-width="1.6"/>
    </marker>
    <pattern id="grid-5mm" x="150" y="61" width="29.52" height="29.51" patternUnits="userSpaceOnUse">
      <path d="M0,0 H29.52 M0,0 V29.51" fill="none" stroke="#d2d2d2" stroke-width="1.2"/>
    </pattern>
    <pattern id="dots-5mm" x="1076.2" y="46.2" width="29.52" height="29.51" patternUnits="userSpaceOnUse">
      <circle cx="14.76" cy="14.76" r="1.5" fill="#a9a9a9"/>
    </pattern>
  </defs>

  <!-- Square grid page -->
  <g class="grid-page">
    <rect class="page" x="141" y="46" width="874" height="1240"/>
    <rect x="150" y="61" width="856" height="1210" fill="url(#grid-5mm)"/>
    <rect class="grid-frame" x="150" y="61" width="856" height="1210"/>
  </g>

  <!-- Dot grid page -->
  <g class="dot-page">
    <rect class="page" x="1083" y="46" width="874" height="1240"/>
    <rect x="1083" y="53" width="874" height="1230" fill="url(#dots-5mm)"/>
  </g>

  <!-- Grid page dimensions -->
  <g class="grid-dimensions">
    <line class="ext-line" x1="24" y1="46" x2="138" y2="46"/>
    <line class="ext-line" x1="24" y1="1286" x2="138" y2="1286"/>
    <line class="ext-line" x1="72" y1="61" x2="145" y2="61"/>
    <line class="ext-line" x1="72" y1="1271" x2="145" y2="1271"/>
    <line class="ext-line" x1="118" y1="90" x2="145" y2="90"/>
    <line class="dim-line" x1="36" y1="46" x2="36" y2="1286" marker-start="url(#arrow-end)" marker-end="url(#arrow-end)"/>
    <line class="dim-line" x1="79" y1="61" x2="79" y2="1271" marker-start="url(#arrow-end)" marker-end="url(#arrow-end)"/>
    <line class="dim-line" x1="124" y1="61" x2="124" y2="90" marker-start="url(#arrow-end)" marker-end="url(#arrow-end)"/>
    <rect class="dim-gap" x="22" y="620" width="30" height="112"/>
    <rect class="dim-gap" x="65" y="620" width="30" height="112"/>
    <text class="dim-label" transform="translate(35 672) rotate(-90)">210 mm</text>
    <text class="dim-label" transform="translate(78 674) rotate(-90)">205 mm</text>
    <text class="dim-label" transform="translate(106 86) rotate(-90)">5 mm</text>

    <line class="ext-line" x1="150" y1="28" x2="150" y2="52"/>
    <line class="ext-line" x1="179" y1="28" x2="179" y2="52"/>
    <line class="dim-line" x1="150" y1="36" x2="179" y2="36" marker-start="url(#arrow-end)" marker-end="url(#arrow-end)"/>
    <text class="dim-label" x="164" y="16">5 mm</text>

    <line class="ext-line" x1="150" y1="1274" x2="150" y2="1320"/>
    <line class="ext-line" x1="1006" y1="1274" x2="1006" y2="1320"/>
    <line class="ext-line" x1="141" y1="1290" x2="141" y2="1366"/>
    <line class="ext-line" x1="1015" y1="1290" x2="1015" y2="1366"/>
    <line class="dim-line" x1="150" y1="1312" x2="1006" y2="1312" marker-start="url(#arrow-end)" marker-end="url(#arrow-end)"/>
    <line class="dim-line" x1="141" y1="1358" x2="1015" y2="1358" marker-start="url(#arrow-end)" marker-end="url(#arrow-end)"/>
    <rect class="dim-gap" x="535" y="1296" width="117" height="32"/>
    <rect class="dim-gap" x="535" y="1342" width="117" height="32"/>
    <text class="dim-label" x="594" y="1312">145 mm</text>
    <text class="dim-label" x="594" y="1357">148 mm</text>
  </g>

  <!-- Dot page dimensions -->
  <g class="dot-dimensions">
    <line class="ext-line" x1="1962" y1="46" x2="2076" y2="46"/>
    <line class="ext-line" x1="1962" y1="1286" x2="2076" y2="1286"/>
    <line class="ext-line" x1="1952" y1="61" x2="2026" y2="61"/>
    <line class="ext-line" x1="1952" y1="1271" x2="2026" y2="1271"/>
    <line class="ext-line" x1="1952" y1="90" x2="1982" y2="90"/>
    <line class="dim-line" x1="2062" y1="46" x2="2062" y2="1286" marker-start="url(#arrow-end)" marker-end="url(#arrow-end)"/>
    <line class="dim-line" x1="2019" y1="61" x2="2019" y2="1271" marker-start="url(#arrow-end)" marker-end="url(#arrow-end)"/>
    <line class="dim-line" x1="1975" y1="61" x2="1975" y2="90" marker-start="url(#arrow-end)" marker-end="url(#arrow-end)"/>
    <rect class="dim-gap" x="2047" y="620" width="30" height="112"/>
    <rect class="dim-gap" x="2004" y="620" width="30" height="112"/>
    <text class="dim-label" transform="translate(2063 672) rotate(90)">210 mm</text>
    <text class="dim-label" transform="translate(2020 674) rotate(90)">205 mm</text>
    <text class="dim-label" transform="translate(1991 90) rotate(90)">5 mm</text>

    <line class="ext-line" x1="1918" y1="30" x2="1918" y2="54"/>
    <line class="ext-line" x1="1948" y1="30" x2="1948" y2="54"/>
    <line class="dim-line" x1="1918" y1="38" x2="1948" y2="38" marker-start="url(#arrow-end)" marker-end="url(#arrow-end)"/>
    <text class="dim-label" x="1931" y="18">5 mm</text>

    <line class="ext-line" x1="1091" y1="1276" x2="1091" y2="1320"/>
    <line class="ext-line" x1="1948" y1="1276" x2="1948" y2="1320"/>
    <line class="ext-line" x1="1083" y1="1290" x2="1083" y2="1366"/>
    <line class="ext-line" x1="1957" y1="1290" x2="1957" y2="1366"/>
    <line class="dim-line" x1="1091" y1="1312" x2="1948" y2="1312" marker-start="url(#arrow-end)" marker-end="url(#arrow-end)"/>
    <line class="dim-line" x1="1083" y1="1358" x2="1957" y2="1358" marker-start="url(#arrow-end)" marker-end="url(#arrow-end)"/>
    <rect class="dim-gap" x="1476" y="1296" width="117" height="32"/>
    <rect class="dim-gap" x="1476" y="1342" width="117" height="32"/>
    <text class="dim-label" x="1535" y="1312">145 mm</text>
    <text class="dim-label" x="1535" y="1357">148 mm</text>
  </g>
</svg>
</body>
</html>
```